Business Card Design Project

Need a business card that stands my education platform as a whole but

Target Market(s)

Parents, families, expats in the middle east.

Industry/Entity Type

Education

Contact Information for Business Card

www.brightlane.ae
www.homesteadhub.ae
www.littlenestcarers.ae

+971552419736
helena@brightlane.ae

Font styles to use
Serif

Requirements
Must have
• Logo's and contact details

```html
<!DOCTYPE html>
<html lang="en">
<head>
<meta charset="utf-8">
<title>Brightlane Business Card</title>
<link href="https://fonts.googleapis.com/css2?family=Yellowtail&family=Source+Sans+3:wght@400;600;700&display=swap" rel="stylesheet">
<style>
  :root {
    --backdrop: #e3e4e6;
    --card: #ffffff;
    --card-shadow: #5a5a5a;
    --teal: #3d8aa3;
    --orange: #f08a2c;
  }
  * { margin: 0; padding: 0; box-sizing: border-box; }
  html, body { width: 1200px; height: 800px; overflow: hidden; }
  body {
    background: var(--backdrop);
    font-family: "Source Sans 3", Arial, sans-serif;
    position: relative;
  }
  .card {
    position: absolute;
    left: 325px;
    width: 545px;
    height: 315px;
    background: var(--card);
    border-radius: 26px;
    box-shadow: 6px 6px 0 var(--card-shadow);
  }
  .card--front { top: 68px; }
  .card--back { top: 420px; }

  .quote {
    position: absolute;
    left: 0;
    top: 90px;
    width: 460px;
    text-align: center;
    font-family: "Yellowtail", cursive;
    color: var(--orange);
    font-size: 27px;
    line-height: 50px;
  }
  .quote-author {
    position: absolute;
    left: 254px;
    top: 190px;
    color: var(--teal);
    font-size: 16px;
  }

  .brand-mark {
    position: absolute;
    display: flex;
    align-items: center;
    gap: 6px;
    color: var(--teal);
    font-weight: 600;
  }
  .brand-mark .dot {
    border-radius: 50%;
    background: var(--teal);
  }
  .brand-mark--small { left: 448px; top: 250px; font-size: 13px; }
  .brand-mark--small .dot { width: 10px; height: 10px; }
  .brand-mark--large { left: 84px; top: 122px; font-size: 24px; }
  .brand-mark--large .dot { width: 18px; height: 18px; }

  .brace {
    position: absolute;
    left: 222px;
    top: 102px;
  }

  .contact-head {
    position: absolute;
    left: 292px;
    top: 72px;
    width: 200px;
  }
  .person-name {
    color: var(--teal);
    font-size: 20px;
    font-weight: 700;
    letter-spacing: 0.5px;
    line-height: 24px;
    white-space: nowrap;
  }
  .divider {
    border-bottom: 1.5px dashed var(--teal);
    margin: 2px 0 3px;
  }
  .person-role {
    color: var(--orange);
    font-size: 14px;
    font-weight: 700;
    letter-spacing: 0.5px;
  }
  .site-list {
    position: absolute;
    left: 292px;
    top: 128px;
    list-style: none;
    color: var(--orange);
    font-size: 15px;
    line-height: 27.5px;
  }
  .contact-line {
    position: absolute;
    top: 255px;
    display: flex;
    align-items: center;
    gap: 14px;
    color: var(--orange);
    font-size: 15px;
  }
  .contact-line--phone { left: 60px; }
  .contact-line--mail { left: 283px; top: 252px; }
</style>
</head>
<body>
  <section class="card card--front">
    <p class="quote">“We must teach our children<br>to dream with their eyes open.”</p>
    <p class="quote-author">— Daniel Ashford —</p>
    <div class="brand-mark brand-mark--small"><span class="dot"></span>Brightlane</div>
  </section>

  <section class="card card--back">
    <div class="brand-mark brand-mark--large"><span class="dot"></span>Brightlane</div>

    <svg class="brace" width="40" height="112" viewBox="0 0 40 112" aria-hidden="true">
      <path d="M6 4 C22 4 24 10 24 24 L24 44 C24 52 28 55 36 56 C28 57 24 60 24 68 L24 88 C24 102 22 108 6 108"
            fill="none" stroke="var(--teal)" stroke-width="7"/>
    </svg>

    <div class="contact-head">
      <p class="person-name">HELENA VARGA</p>
      <div class="divider"></div>
      <p class="person-role">MUM</p>
    </div>

    <ul class="site-list">
      <li>brightlane.ae</li>
      <li>littlenestcarers.ae</li>
      <li>homesteadhub.ae</li>
    </ul>

    <div class="contact-line contact-line--phone">
      <svg width="18" height="18" viewBox="0 0 18 18" aria-hidden="true">
        <circle cx="9" cy="9" r="8" fill="none" stroke="var(--teal)" stroke-width="1.5"/>
        <path d="M6.2 4.8 L7.6 6.6 L6.9 7.6 C7.4 8.8 8.3 9.8 9.6 10.5 L10.6 9.8 L12.4 11.2 L11.6 12.6 C8.6 12.6 5.4 9.4 5.2 6 Z" fill="var(--teal)"/>
      </svg>
      <span>+971552419736</span>
    </div>

    <div class="contact-line contact-line--mail">
      <svg width="20" height="15" viewBox="0 0 20 15" aria-hidden="true">
        <rect x="1" y="1" width="18" height="13" fill="none" stroke="var(--teal)" stroke-width="1.5"/>
        <path d="M1 1 L10 8.5 L19 1 M1 14 L7.5 7 M19 14 L12.5 7" fill="none" stroke="var(--teal)" stroke-width="1.5"/>
      </svg>
      <span>helena@brightlane.ae</span>
    </div>
  </section>
</body>
</html>
```